Business Name is TB Glamworks - Make-up Artist

I'm looking for an attractive and eye catching business card for for mobile make-up artist business. On the front of the card, I just want the name TB Glamworks in feminine type cursive writing and underneath my name Tessa Bourne and Make-Up Artist.
On the back of the card, I would like written down one side the following;
Make-Up Tutorials
Bridal
Photography
Debutante
Formals
Family Portraits
I would also like the following details as well as the Chatterbook and Pictoflow Icons;
Mobile: 0482 615 379
Email: tessabourne@maildrop-example.com
Website: tessabourne.velqora-example.com
Certificate III in Make-Up
Also, I would like a section that says Your Next Appointment and a space to put that information.
I would also like the Velqora Symbol on the bottom right hand corner (I have attached)

Target Market(s)

Mostly females

Industry/Entity Type

Makeup

Contact Information for Business Card

TB Glamworks
Tessa Bourne - Make-Up Artist

Font styles to use
Script

Colors
b768aa
886aae
e34297

Requirements
Must have
• Mobile: 0482 615 379
• Email: tessabourne@maildrop-example.com
• Website: tessabourne.velqora-example.com
• Certificate III in Make-Up
Nice to have
• Something to do with make-up like a smudged lipstick or some eye shadow
Should not have
• Don't want it too busy

```html
<!DOCTYPE html>
<html lang="en">
<head>
<meta charset="utf-8">
<title>TB Glamworks - Make-up Artist</title>
<link rel="stylesheet" href="https://fonts.googleapis.com/css2?family=Great+Vibes&family=Questrial&family=Didact+Gothic&display=swap">
<style>
  :root {
    --stage: #1a1a1a;
    --card: #fafafa;
    --pink: #e0167a;
    --purple: #6c5fa3;
    --ink: #4a4a4a;
    --brand-green: #0f8a3c;
    --white: #ffffff;
  }
  html, body { margin: 0; padding: 0; overflow: hidden; }
  body {
    width: 1200px; height: 1118px;
    background: var(--stage);
    position: relative;
    font-family: "Questrial", "Didact Gothic", sans-serif;
    color: var(--ink);
  }
  .card {
    position: absolute;
    left: 292px;
    width: 615px; height: 372px;
    background: var(--card);
    overflow: hidden;
  }
  .card--appointment { top: 168px; }
  .card--contact { top: 578px; }

  .wordmark {
    position: absolute;
    font-family: "Great Vibes", cursive;
    white-space: nowrap;
    line-height: 1;
  }
  .wordmark .initials { color: var(--pink); }
  .wordmark .studio { color: var(--purple); }
  .card--appointment .wordmark { left: 0; right: 0; top: 50px; text-align: center; font-size: 74px; }
  .card--contact .wordmark { left: 32px; top: 58px; font-size: 80px; }

  .field {
    position: absolute;
    font-size: 17px;
    display: flex;
    align-items: flex-end;
  }
  .field .rule { flex: 1; border-bottom: 1px solid var(--ink); margin-left: 5px; height: 15px; }
  .field--name { left: 43px; top: 173px; width: 529px; }
  .field--date { left: 43px; top: 220px; width: 321px; }
  .field--time { left: 370px; top: 220px; width: 202px; }

  .services-band {
    position: absolute;
    left: 0; top: 282px;
    width: 494px; height: 62px;
    background: var(--pink);
    color: var(--white);
    font-size: 17px;
    box-sizing: border-box;
    padding: 8px 0 0 44px;
    line-height: 25px;
  }
  .services-band .sep { margin: 0 10px; }
  .band-end {
    position: absolute;
    left: 586px; top: 282px;
    width: 29px; height: 62px;
    background: var(--pink);
  }

  .partner {
    position: absolute;
    display: flex; flex-direction: column; align-items: center;
    color: var(--brand-green);
    font-family: "Questrial", sans-serif;
    letter-spacing: 1px;
  }
  .partner .dot { border-radius: 50%; background: var(--brand-green); }
  .card--appointment .partner { left: 500px; top: 280px; width: 76px; font-size: 14px; }
  .card--appointment .partner .dot { width: 36px; height: 36px; margin-bottom: 8px; }
  .card--contact .partner { left: 500px; top: 44px; width: 96px; font-size: 16px; }
  .card--contact .partner .dot { width: 46px; height: 46px; margin-bottom: 10px; }

  .contacts {
    position: absolute;
    left: 46px; top: 170px;
    margin: 0; padding: 0; list-style: none;
    font-size: 16px;
  }
  .contacts li { display: flex; align-items: center; height: 25px; }
  .contacts svg { width: 14px; height: 14px; margin-right: 18px; fill: var(--pink); }
  .follow {
    position: absolute;
    left: 47px; top: 252px;
    font-size: 16px;
  }
  .follow .network { color: var(--purple); }

  .waves { position: absolute; left: 0; top: 0; width: 615px; height: 372px; }

  .signature {
    position: absolute;
    right: 30px; top: 274px;
    text-align: right;
    color: var(--white);
  }
  .signature .person { font-size: 25px; font-weight: 700; font-family: "Didact Gothic", sans-serif; letter-spacing: 0.3px; margin-bottom: 4px; }
  .signature .role { font-size: 15px; font-style: italic; line-height: 20px; }
</style>
</head>
<body>

<section class="card card--appointment">
  <div class="wordmark"><span class="initials">TB</span> <span class="studio">Glamworks</span></div>
  <div class="field field--name">Name:<span class="rule"></span></div>
  <div class="field field--date">Date:<span class="rule"></span></div>
  <div class="field field--time">Time:<span class="rule"></span></div>
  <div class="services-band">
    Make-Up Tutorials<span class="sep">|</span>Bridal<span class="sep">|</span>Photography<br>
    Debutante<span class="sep">|</span>Formals<span class="sep">|</span>Family Portraits
  </div>
  <div class="band-end"></div>
  <div class="partner"><span class="dot"></span>VELQORA</div>
</section>

<section class="card card--contact">
  <svg class="waves" viewBox="0 0 615 372" aria-hidden="true">
    <path d="M0,372 L0,335 C130,362 250,338 365,288 C455,248 540,220 615,218 L615,372 Z" fill="var(--purple)"/>
    <path d="M0,298 C110,345 235,342 352,282 C452,232 540,198 615,196 L615,206 C540,210 452,242 362,290 C240,354 110,360 0,322 Z" fill="var(--pink)"/>
    <path d="M55,308 C160,332 270,330 350,300 C270,338 160,340 55,308 Z" fill="var(--pink)"/>
  </svg>
  <div class="wordmark"><span class="initials">TB</span> <span class="studio">Glamworks</span></div>
  <div class="partner"><span class="dot"></span>VELQORA</div>
  <ul class="contacts">
    <li><svg viewBox="0 0 16 16"><path d="M2,6 C2,3 14,3 14,6 L11,7 L10,5 L6,5 L5,7 Z M4,8 L12,8 L14,13 L2,13 Z"/></svg>0482 615 379</li>
    <li><svg viewBox="0 0 16 16"><path d="M1,3 L15,3 L15,13 L1,13 Z M2.5,4.5 L8,9 L13.5,4.5 Z" fill-rule="evenodd"/></svg>tessabourne@maildrop-example.com</li>
    <li><svg viewBox="0 0 16 16"><circle cx="8" cy="8" r="6.5" fill="none" stroke="var(--pink)" stroke-width="1.5"/><path d="M1.5,8 L14.5,8 M8,1.5 C4,5 4,11 8,14.5 C12,11 12,5 8,1.5" fill="none" stroke="var(--pink)" stroke-width="1.3"/></svg>tessabourne.velqora-example.com</li>
  </ul>
  <div class="follow">Follow on: <span class="network">Chatterbook</span> · <span class="network">Pictoflow</span></div>
  <div class="signature">
    <div class="person">Tessa Bourne</div>
    <div class="role">Make-Up Artist</div>
    <div class="role">Certificate III in Make-Up</div>
  </div>
</section>

</body>
</html>
```